Kandor Lune Studios App Interface Design

Start Up Company Kandor Lune Studios needs design and colour for its App interface. App for Velto/Zarpix/Zarpix mini. App allows customers to connect to our self serve kiosk and browse and download entertainment content. Kiosks will be placed in international airport departure lounges initially. Final design should be a great looking, modern feel that keeps with the style of the rest of our elements. Screenshots attached.

```html
<!DOCTYPE html>
<html lang="en">
<head>
<meta charset="utf-8">
<title>Kandor Lune Studios – Movies For Traveller</title>
<link rel="stylesheet" href="https://fonts.googleapis.com/css2?family=Oswald:wght@400;600&family=Roboto:wght@400&display=swap">
<style>
  :root {
    --deep-blue: #1b4a86;
    --mid-blue: #2f86cc;
    --cyan: #48d4ee;
    --title-cyan: #5ee3f2;
    --white: #ffffff;
    --status-bg: #111417;
    --status-text: #c9ccd0;
    --kiosk-blue: #1f5fb4;
    --kiosk-dark: #163a6e;
  }
  * { margin: 0; padding: 0; box-sizing: border-box; }
  html, body { width: 938px; height: 1200px; overflow: hidden; background: var(--deep-blue); }
  .app-screen { position: relative; width: 938px; height: 1200px; overflow: hidden; font-family: "Oswald", sans-serif; }
  .backdrop { position: absolute; inset: 0; width: 938px; height: 1200px; }
  .status-bar {
    position: absolute; top: 0; left: 0; right: 0; height: 24px;
    background: var(--status-bg); color: var(--status-text);
    font-family: "Roboto", sans-serif; font-size: 12px;
    display: flex; align-items: center; justify-content: space-between; padding: 0 10px;
  }
  .status-bar .battery { width: 24px; height: 11px; border: 1px solid var(--status-text); border-radius: 2px; padding: 1px; }
  .status-bar .battery span { display: block; height: 100%; background: var(--status-text); }
  .brand {
    position: absolute; top: 132px; left: 189px; width: 560px;
    display: flex; align-items: center; gap: 28px;
  }
  .brand-mark { flex: none; width: 104px; height: 104px; border: 5px solid var(--white); border-radius: 10px; }
  .brand-name { color: var(--white); font-weight: 600; font-size: 50px; letter-spacing: 1px; text-transform: uppercase; line-height: 1; white-space: nowrap; }
  .kiosk-visual {
    position: absolute; left: 327px; top: 311px; width: 283px; height: 500px;
    background: linear-gradient(180deg, var(--kiosk-dark), var(--kiosk-blue) 60%, var(--kiosk-dark));
    border-radius: 14px 14px 6px 6px; opacity: .9;
  }
  .screen-title {
    position: absolute; top: 876px; left: 0; right: 0; text-align: center;
    color: var(--title-cyan); font-weight: 400; font-size: 63px; line-height: 1;
  }
  .play-button { position: absolute; left: 416px; top: 968px; width: 104px; height: 104px; }
</style>
</head>
<body>
<main class="app-screen">
  <svg class="backdrop" viewBox="0 0 938 1200" aria-hidden="true">
    <defs>
      <linearGradient id="wave-light" x1="0" y1="0" x2="1" y2="0">
        <stop offset="0" stop-color="#46d0ec"/>
        <stop offset="0.55" stop-color="#35a9dc"/>
        <stop offset="1" stop-color="#2273bd"/>
      </linearGradient>
      <linearGradient id="wave-mid" x1="0" y1="0" x2="1" y2="1">
        <stop offset="0" stop-color="#2f8fd0"/>
        <stop offset="1" stop-color="#1c5ea6"/>
      </linearGradient>
      <linearGradient id="top-sky" x1="0" y1="0" x2="0" y2="1">
        <stop offset="0" stop-color="#1a4a8a"/>
        <stop offset="1" stop-color="#1e5aa0"/>
      </linearGradient>
    </defs>
    <rect width="938" height="1200" fill="url(#top-sky)"/>
    <path d="M0 330 C220 250 420 420 600 420 C760 420 860 300 938 250 L938 1200 L0 1200 Z" fill="#2468b2"/>
    <path d="M0 500 C260 420 520 560 938 600 L938 1200 L0 1200 Z" fill="url(#wave-light)"/>
    <path d="M0 760 C300 700 620 840 938 820 L938 1200 L0 1200 Z" fill="url(#wave-mid)"/>
    <path d="M0 1000 C320 1040 640 1110 938 1090 L938 1200 L0 1200 Z" fill="#2a7dc6"/>
    <path d="M0 1180 C300 1150 640 1200 938 1160 L938 1200 L0 1200 Z" fill="#1d4f94"/>
  </svg>

  <header class="status-bar">
    <span class="device-name">Zarpix</span>
    <span class="clock">8:35 PM</span>
    <span class="battery"><span></span></span>
  </header>

  <div class="brand">
    <div class="brand-mark"></div>
    <div class="brand-name">Kandor Lune Studios</div>
  </div>

  <div class="kiosk-visual" role="img" aria-label="Illustration of a tall curved blue movie download kiosk standing on a dark base"></div>

  <h1 class="screen-title">Movies For Traveller</h1>

  <svg class="play-button" viewBox="0 0 104 104" role="img" aria-label="Play">
    <defs>
      <radialGradient id="play-fill" cx="0.45" cy="0.35" r="0.7">
        <stop offset="0" stop-color="#6fe3f5"/>
        <stop offset="1" stop-color="#1f9fd6"/>
      </radialGradient>
    </defs>
    <circle cx="52" cy="52" r="50" fill="url(#play-fill)" stroke="#1a6fb3" stroke-width="2"/>
    <path d="M41 36 L70 52 L41 68 Z" fill="#ffffff"/>
  </svg>
</main>
</body>
</html>
```